Facebook Cover & Profile Branding for VelbrooK Systems

We need a modern, premium Facebook cover image for our company Velbrook Systems GmbH. The design should be clean, professional, and aligned with our corporate colors (neon green and deep blue) as well as our logo. It should clearly represent us as a technology and IT consulting company with a strong focus on software testing and quality assurance.

Since Velbrook Systems is also active in the U.S. market, the design may include global or U.S.-related elements (e.g., subtle references to international presence, tech innovation with a global reach).

Requirements:

Integration of the Velbrook logo and brand colors

Modern, premium look with a tech-driven feel

Clear, simple layout that looks good on desktop and mobile

Optional: subtle U.S./international references to highlight our global presence

Goal:
A professional, eye-catching Facebook cover image that strengthens our brand identity and reflects our international expansion into the U.S. market.

Target Market(s)

Medium to large enterprises in the technology, finance, and energy sectors - Companies looking for premium IT consulting, software testing, and quality assurance services - Decision makers and executives (CIOs, CTOs, IT managers) in Europe and the United States - A global audience that values innovation, professionalism, and trust

Industry/Entity Type

Information Technology & Consulting Software Testing & Quality Assurance Technology / Professional Services Global IT Consulting with U.S. Market Presence

Requirements
Must have
• Integration of the Velbrook Systems logo and brand colors (Neon Green & Deep Blue) Modern, premium design with a strong tech-oriented look and feel Clean and professional layout, optimized for both desktop and mobile display Clear visibility of the brand identity (technology, IT consulting, software testing, quality assurance) Subtle reference to U.S. presence / global expansion (to highlight activity in both Germany and the U.S.) Balanced use of colors and space for a high-end, corporate appearance
Nice to have
• Subtle animations or motion effects (e.g., light gradients, moving lines, glowing accents) Dark/Light version option for different moods or seasonal campaigns Integration of social media icons (LinkedIn, Instagram, Facebook) in a clean, minimal way Tech-inspired background elements (digital patterns, abstract shapes, network grids) Space for an optional tagline or slogan (e.g., “Innovation. Quality. Global Impact.”) Adaptability for other platforms (so the design style can be reused for LinkedIn or Twitter headers)
Should not have
• Cluttered or overloaded layouts that reduce clarity Low-quality stock photos or generic imagery that doesn’t fit a premium brand Use of colors outside the Velbrook brand identity (Neon Green & Deep Blue) Outdated design styles (e.g., heavy gradients, 3D effects, drop shadows) Complex text blocks that make the design look busy Elements that distract from the logo and core brand message Pop-art or playful styles that don’t match the premium, professional tech look

```html
<!DOCTYPE html>
<html lang="en">
<head>
<meta charset="utf-8">
<title>Velbrook Systems GmbH – Facebook Branding Set</title>
<link rel="stylesheet" href="https://fonts.googleapis.com/css2?family=Archivo+Black&family=Outfit:wght@400;500&family=Montserrat:wght@500&display=swap">
<style>
  :root {
    --board: #e3e3e3;
    --label: #2e2e2e;
    --base: #2a2a2b;
    --neon: #35e62c;
    --neon-soft: #3d7a3a;
    --deep-blue: #1060f0;
    --blue-glow: #2c5aa0;
    --white: #ffffff;
    --headline-blue: #c9dcff;
    --headline-green: #dcf7dc;
    --box-fill: #3a3c3f;
    --box-edge: #3fb04a;
    --cta-ink: #1b3a1a;
    --wave-teal: #4a8fb0;
    --wave-blue: #2d63b5;
  }
  * { margin: 0; padding: 0; box-sizing: border-box; }
  html, body { width: 1200px; height: 1101px; overflow: hidden; }
  body { background: var(--board); position: relative; font-family: "Outfit", sans-serif; }

  .board-label {
    position: absolute;
    font-family: "Montserrat", sans-serif;
    font-weight: 500;
    font-size: 23px;
    letter-spacing: 2px;
    color: var(--label);
    transform: translateX(-50%);
    white-space: nowrap;
  }
  .label-profile { left: 332px; top: 44px; }
  .label-post { left: 867px; top: 44px; }
  .label-cover { left: 600px; top: 1036px; }

  .panel {
    position: absolute;
    overflow: hidden;
    background:
      radial-gradient(ellipse 45% 45% at 100% 0%, rgba(61,122,58,0.95), rgba(61,122,58,0) 100%),
      radial-gradient(ellipse 40% 55% at 0% 68%, rgba(44,90,160,0.85), rgba(44,90,160,0) 100%),
      var(--base);
  }
  .profile-picture { left: 80px; top: 85px; width: 505px; height: 505px; }
  .facebook-post { left: 614px; top: 85px; width: 505px; height: 505px; }
  .cover-banner { left: 80px; top: 620px; width: 1040px; height: 396px;
    background:
      radial-gradient(ellipse 30% 45% at 100% 0%, rgba(61,122,58,0.95), rgba(61,122,58,0) 100%),
      radial-gradient(ellipse 25% 60% at 0% 85%, rgba(44,90,160,0.7), rgba(44,90,160,0) 100%),
      var(--base);
  }

  .wave-field { position: absolute; }
  .post-wave {
    left: 0; bottom: 0; width: 100%; height: 120px;
    background: linear-gradient(180deg, rgba(74,143,176,0) 0%, rgba(74,143,176,0.45) 45%, rgba(45,99,181,0.75) 100%);
  }
  .cover-wave {
    left: 0; bottom: 0; width: 100%; height: 150px;
    background: linear-gradient(180deg, rgba(74,143,176,0) 0%, rgba(74,143,176,0.4) 50%, rgba(45,99,181,0.8) 100%);
  }

  .brand { position: absolute; display: flex; align-items: center; color: var(--white); font-family: "Outfit", sans-serif; font-weight: 500; white-space: nowrap; }
  .brand-dot { border-radius: 50%; background: var(--neon); flex: none; }

  .profile-brand { left: 50%; top: 50%; transform: translate(-50%, -50%); gap: 16px; font-size: 40px; }
  .profile-brand .brand-dot { width: 34px; height: 34px; }

  .post-brand { left: 50%; top: 62px; transform: translateX(-50%); gap: 10px; font-size: 17px; }
  .post-brand .brand-dot { width: 20px; height: 20px; }

  .cover-brand { left: 60px; top: 96px; gap: 14px; font-size: 27px; }
  .cover-brand .brand-dot { width: 34px; height: 34px; }

  .headline { position: absolute; font-family: "Archivo Black", sans-serif; color: var(--white); white-space: nowrap; line-height: 1; }
  .headline-tech {
    background: linear-gradient(90deg, var(--headline-blue) 0%, var(--white) 50%, var(--headline-green) 100%);
    -webkit-background-clip: text; background-clip: text; color: transparent;
  }
  .accent-dot { color: var(--neon); }

  .enabling-box {
    position: absolute;
    background: linear-gradient(180deg, #45474b, var(--box-fill));
    border: 1.5px solid var(--box-edge);
    border-radius: 4px;
    display: flex; align-items: center;
  }
  .enabling-box .headline { position: static; }

  /* post sizes */
  .post-empowering { left: 50%; transform: translateX(-50%); top: 139px; font-size: 31px; letter-spacing: -1.8px; }
  .post-technology { left: 50%; transform: translateX(-50%); top: 174px; font-size: 44px; letter-spacing: -3px; }
  .post-enabling-box { left: 89px; top: 229px; width: 224px; height: 51px; padding-left: 25px; }
  .post-enabling-box .headline { font-size: 30px; letter-spacing: -1.8px; }
  .post-success { left: 182px; top: 297px; font-size: 44px; letter-spacing: -2.6px; }

  .tagline {
    position: absolute; left: 0; right: 0; top: 356px;
    text-align: center; color: var(--white);
    font-size: 20px; line-height: 25px; font-weight: 400;
  }

  .cta { position: absolute; left: 102px; top: 434px; height: 36px; display: flex; }
  .cta-label, .cta-phone {
    height: 36px; display: flex; align-items: center; transform: skewX(-18deg);
  }
  .cta-label { width: 135px; background: var(--deep-blue); border-radius: 4px 0 0 4px; justify-content: center; }
  .cta-phone { width: 168px; background: var(--neon); border-radius: 0 4px 4px 0; padding-left: 14px; gap: 6px; }
  .cta-label span, .cta-phone > * { transform: skewX(18deg); }
  .cta-label span { color: var(--white); font-size: 17px; font-weight: 500; }
  .cta-phone span { color: var(--cta-ink); font-size: 14px; font-weight: 500; letter-spacing: -0.3px; }
  .cta-phone svg { width: 13px; height: 13px; }

  /* cover sizes */
  .cover-empowering { left: 516px; top: 62px; font-size: 52px; letter-spacing: -3px; }
  .cover-technology { left: 445px; top: 110px; font-size: 70px; letter-spacing: -4.6px; }
  .cover-enabling-box { left: 447px; top: 194px; width: 332px; height: 76px; padding-left: 36px; }
  .cover-enabling-box .headline { font-size: 46px; letter-spacing: -2.6px; }
  .cover-success { left: 584px; top: 292px; font-size: 66px; letter-spacing: -4px; }
</style>
</head>
<body>
  <div class="board-label label-profile">PROFILE PICTURE</div>
  <div class="board-label label-post">FACEBOOK POST</div>

  <section class="panel profile-picture">
    <div class="brand profile-brand"><span class="brand-dot"></span>Velbrook</div>
  </section>

  <section class="panel facebook-post">
    <div class="wave-field post-wave" role="img" aria-label="Flowing digital particle wave in teal and blue"></div>
    <div class="brand post-brand"><span class="brand-dot"></span>Velbrook Systems GmbH</div>
    <h2 class="headline post-empowering">EMPOWERING</h2>
    <h2 class="headline headline-tech post-technology">TECHNOLOGY.</h2>
    <div class="enabling-box post-enabling-box"><span class="headline">ENABLING</span></div>
    <h2 class="headline post-success">SUCCESS<span class="accent-dot">.</span></h2>
    <p class="tagline">Excellent software quality.<br>Globally minded.</p>
    <div class="cta">
      <div class="cta-label"><span>Reach Us!</span></div>
      <div class="cta-phone">
        <svg viewBox="0 0 24 24" aria-hidden="true"><path fill="#1b3a1a" d="M6.6 10.8a15.1 15.1 0 0 0 6.6 6.6l2.2-2.2a1 1 0 0 1 1-.25 11.4 11.4 0 0 0 3.6.57 1 1 0 0 1 1 1V20a1 1 0 0 1-1 1A17 17 0 0 1 3 4a1 1 0 0 1 1-1h3.5a1 1 0 0 1 1 1c0 1.25.2 2.45.57 3.57a1 1 0 0 1-.25 1z"/></svg>
        <span>+49 3581 40720-18</span>
      </div>
    </div>
  </section>

  <section class="panel cover-banner">
    <div class="wave-field cover-wave" role="img" aria-label="Flowing digital particle wave in teal and blue"></div>
    <div class="brand cover-brand"><span class="brand-dot"></span>Velbrook Systems GmbH</div>
    <h1 class="headline cover-empowering">EMPOWERING</h1>
    <h1 class="headline headline-tech cover-technology">TECHNOLOGY.</h1>
    <div class="enabling-box cover-enabling-box"><span class="headline">ENABLING</span></div>
    <h1 class="headline cover-success">SUCCESS<span class="accent-dot">.</span></h1>
  </section>

  <div class="board-label label-cover">FACEBOOK COVER BANNER</div>
</body>
</html>
```